Bridgeway, Lantern, and the Quiet Harbor Loop Research Program Website

Overview: This website will serve a new research program (Bridgeway, Lantern, and the Quiet Harbor Loop) at the Fenmoor University School of Medicine. I want a clean, intuitive design that has a navigation bar, but uses icons/graphic buttons to link to the main pages. In an attached Word document, I have provided a basic information architecture for the site, understanding that this project would just generate graphics and code for the 3 pages. I highlighted the 3 pages I'd like designed.
Target market: People who want to participate in our research, or contribute grant funding to specific projects.
Number of page: The design project focuses on 3 pages, but the site must accommodate 6 pages with top-level links. See attached Word doc.
Logo and website header: Please integrate our logo in the header. I've uploaded it as a png file--both with the name of the website and with just the logo image. I imaging the logo would look great in a banner set against an image of a mountain. The two main design themes I want to see included are nature and healthcare.
Text content: I have not yet provided text. Use some dummy text.
Technical Specifications:
- Build using WordPress. We will host this site ourselves on Brimloft using WordPress.
- The design package must be coded.
- The template must be responsive to different platforms (e.g., computer, mobile phone, iPad).
Thank you! I look forward to seeing your designs.
- Ned

```html
<!DOCTYPE html>
<html lang="en">
<head>
<meta charset="utf-8">
<title>Bridgeway, Lantern, and the Quiet Harbor Loop</title>
<link rel="stylesheet" href="https://fonts.googleapis.com/css2?family=Exo:wght@600;700;800&family=Roboto:wght@400;500;700&display=swap">
<style>
:root{
  --blue:#1a5b97;
  --blue-dark:#0f3b68;
  --navy:#0b2644;
  --green:#53993f;
  --green-light:#6fae3e;
  --ink:#222;
  --muted:#666;
  --white:#fff;
}
*{box-sizing:border-box;margin:0;padding:0}
html,body{width:1200px;height:4190px;overflow:hidden}
body{position:relative;font-family:'Roboto',sans-serif;color:var(--ink);background:var(--white)}
.abs{position:absolute}
.heading{font-family:'Exo',sans-serif;font-weight:800;text-transform:uppercase;letter-spacing:.5px}
/* header */
.brand{left:110px;top:14px;display:flex;align-items:center;gap:16px}
.brand-mark{width:96px;height:96px;border-radius:50%;background:#e8f1e2;border:3px solid var(--green)}
.brand-divider{width:2px;height:70px;background:var(--blue)}
.brand-name{font-family:'Exo',sans-serif;font-weight:700;font-size:21px;color:var(--blue);line-height:1.2}
.brand-sub{font-family:'Exo',sans-serif;font-weight:700;font-size:16px;color:var(--green)}
.call{left:866px;top:32px;display:flex;align-items:center;gap:14px}
.call-icon{width:48px;height:48px;border:2px solid var(--blue);border-radius:50%;display:flex;align-items:center;justify-content:center}
.call small{display:block;font-size:14px;font-weight:500}
.call strong{font-size:21px;font-weight:700}
.nav{left:0;top:122px;width:1200px;height:60px;background:var(--blue)}
.nav a{position:absolute;top:0;height:60px;line-height:60px;color:#fff;font-weight:700;font-size:15px;text-decoration:none}
.nav .active{background:var(--green);padding:0 11px}
.nav .book{left:833px;width:257px;text-align:center;background:var(--green)}
/* hero */
.hero{left:0;top:182px;width:1200px;height:740px;background:linear-gradient(110deg,#9c8a70 0%,#d89a4e 35%,#f4c57a 52%,#8a5a2e 75%,#4a3a2c 100%)}
.hero-title{left:141px;top:380px;font-size:48px;line-height:48px;color:#1f1f1f;width:620px}
.btn{display:inline-block;border-radius:30px;color:#fff;font-weight:700;font-size:14px;text-align:center;background:linear-gradient(90deg,var(--green),var(--blue))}
.hero-btn{left:141px;top:546px;width:163px;height:49px;line-height:49px}
.arrow{width:52px;height:52px;border-radius:50%;display:flex;align-items:center;justify-content:center}
/* about */
.about-mark{left:150px;top:1020px;width:410px;height:380px;display:flex;align-items:center;justify-content:center;gap:16px}
.about-title{left:626px;top:1005px;font-size:54px;color:#1f1f1f}
.about-text{left:626px;top:1080px;width:465px;font-size:13.4px;line-height:22.2px;color:var(--muted)}
.about-btn{left:626px;top:1343px;width:164px;height:49px;line-height:49px}
/* projects */
.projects{left:0;top:1530px;width:1200px;height:920px;background:linear-gradient(180deg,#16395f 0%,#1b4f80 40%,#0c2545 100%)}
.section-title{width:1200px;left:0;text-align:center;font-size:40px}
.card{width:470px;height:241px;background:#fff;border:2px solid #ccd;display:flex;padding:6px;gap:20px}
.card-img{width:211px;height:229px;flex:none}
.card h3{font-family:'Roboto',sans-serif;font-weight:700;font-size:19px;line-height:22px;text-transform:uppercase;margin-top:16px;color:#1f1f1f}
.card p{font-size:13.4px;line-height:22px;color:var(--muted);margin-top:14px}
.card a{display:block;margin-top:8px;color:var(--blue);font-weight:700;font-size:14px;text-decoration:none}
/* team */
.member{width:220px;text-align:center}
.member .photo{width:212px;height:212px;border-radius:50%;margin:0 auto}
.member h4{font-size:20px;font-weight:500;margin-top:16px}
.member span{font-size:15px;color:var(--muted)}
/* faq */
.faq-bg{left:0;top:3030px;width:1200px;height:660px;background:linear-gradient(180deg,#5a9e40,#4a8a38)}
.faq{left:294px;width:612px;height:62px;background:#fff;border-radius:3px;font-size:14px;line-height:62px;padding:0 24px;display:flex;justify-content:space-between;align-items:center}
.faq.open{background:var(--blue);color:#fff}
.plus{width:13px;height:13px;border-radius:50%;background:var(--green);color:#fff;font-size:12px;line-height:13px;text-align:center;font-weight:700}
.faq.open .plus{background:#fff;color:var(--blue)}
/* footer */
.footer{left:0;top:3640px;width:1200px;height:550px;background:var(--blue)}
.foot-h{font-size:17px;font-weight:700;color:#fff;letter-spacing:.5px}
.field{background:#fff;font-size:13px;color:#777;padding:10px 18px;height:41px}
.links li{list-style:none;color:#fff;font-size:15px;height:30px}
.links li::before{content:"»";margin-right:12px}
.contact{color:#fff;font-size:15px;line-height:22px;display:flex;gap:14px}
.social{width:30px;height:30px;border-radius:50%}
</style>
</head>
<body>

<header>
  <div class="abs brand">
    <div class="brand-mark"></div>
    <div class="brand-divider"></div>
    <div>
      <div class="brand-name">Bridgeway, Lantern, and the Quiet Harbor Loop</div>
      <div class="brand-sub">The Research Program</div>
    </div>
  </div>
  <div class="abs call">
    <div class="call-icon"><svg width="20" height="20" viewBox="0 0 24 24"><path d="M6.6 10.8a15 15 0 0 0 6.6 6.6l2.2-2.2c.3-.3.7-.4 1-.2 1.1.4 2.3.6 3.6.6.6 0 1 .4 1 1V20c0 .6-.4 1-1 1A17 17 0 0 1 3 4c0-.6.4-1 1-1h3.5c.6 0 1 .4 1 1 0 1.3.2 2.5.6 3.6.1.3 0 .7-.2 1z" fill="var(--green)"/></svg></div>
    <div><small>CALL US TODAY :</small><strong>+1 555 204 7731</strong></div>
  </div>
  <nav class="abs nav">
    <a class="active" style="left:99px">HOME</a>
    <a style="left:204px">PEOPLE</a>
    <a style="left:311px">PROJECTS</a>
    <a style="left:437px">FAQS</a>
    <a style="left:524px">RESOURCES</a>
    <a class="book">BOOK AN APPOINTMENT</a>
  </nav>
</header>

<section>
  <div class="abs hero" role="img" aria-label="Person with outstretched arms on a mountain at sunset"></div>
  <svg class="abs" style="left:0;top:740px" width="1200" height="200" viewBox="0 0 1200 200">
    <path d="M0 95 C200 160 380 140 600 75 C850 0 1050 0 1200 60 V200 H0 Z" fill="var(--blue)"/>
    <path d="M0 95 C200 190 400 170 640 95 C870 30 1050 40 1200 90 V200 H0 Z" fill="var(--green)"/>
    <path d="M0 125 C220 210 420 180 660 115 C880 55 1060 70 1200 110 V200 H0 Z" fill="#fff"/>
  </svg>
  <h1 class="abs heading hero-title">Bridgeway, Lantern,<br>and the Quiet<br>Harbor Loop</h1>
  <a class="abs btn hero-btn">GET STARTED</a>
  <div class="abs arrow" style="left:140px;top:616px;background:var(--blue)"><svg width="14" height="14" viewBox="0 0 14 14"><path d="M9 2 4 7l5 5" stroke="#fff" stroke-width="2" fill="none"/></svg></div>
  <div class="abs arrow" style="left:203px;top:616px;background:#fff"><svg width="14" height="14" viewBox="0 0 14 14"><path d="M5 2l5 5-5 5" stroke="#333" stroke-width="2" fill="none"/></svg></div>
</section>

<section>
  <div class="abs about-mark">
    <div style="width:40px;height:40px;border-radius:50%;background:var(--green)"></div>
    <span style="font-family:'Exo',sans-serif;font-weight:700;font-size:26px;color:var(--blue);line-height:1.3">Bridgeway, Lantern,<br>and the Quiet<br>Harbor Loop</span>
  </div>
  <h2 class="abs heading about-title">About BLQ</h2>
  <p class="abs about-text">Lorem ipsum dolor sit amet, consectetur adipiscing elit, sed do eiusmod tempor incididunt ut labore et dolore magna aliqua. Ut enim ad minim veniam, quis nostrud exercitation ullamco laboris nisi ut aliquip ex ea commodo consequat. Duis aute irure dolor in reprehenderit in voluptate velit esse cillum dolore eu fugiat nulla pariatur. Excepteur sint occaecat cupidatat non proident, sunt in culpa qui officia deserunt mollit anim id est laborum.Lorem ipsum dolor sit amet, consectetur adipiscing elit, sed do eiusmod tempor incididunt ut labore et dolore magna aliqua. Ut enim ad minim veniam, quis nostrud exercitation ullamco laboris nisi ut aliquip ex ea commodo consequat. Duis aute irure dolor in reprehenderit in voluptate velit esse cillum dolore eu fugiat nulla pariatur.</p>
  <a class="abs btn about-btn">LEARN MORE</a>
</section>

<section>
  <div class="abs projects" role="img" aria-label="Silhouette of a person meditating against a dusky blue sky"></div>
  <svg class="abs" style="left:0;top:1440px" width="1200" height="130" viewBox="0 0 1200 130">
    <path d="M0 0 H1200 V30 C1100 -5 900 0 700 55 C500 110 300 140 0 110 Z" fill="#fff"/>
    <path d="M320 160 C600 90 850 20 1000 10 C1100 5 1160 30 1200 60 V20 C1150 -5 1050 -5 950 15 C800 45 600 110 320 160 Z" fill="var(--green)"/>
  </svg>
  <h2 class="abs heading section-title" style="top:1672px;color:#fff">Research Projects</h2>

  <article class="abs card" style="left:111px;top:1754px">
    <div class="card-img" role="img" aria-label="Person meditating before a glowing circle of light" style="background:linear-gradient(160deg,#d9b9c9,#7d6a9b,#2c2c3a)"></div>
    <div><h3>Lorem ipsum dolor sit amet, consectet ur adipiscing</h3><p>Duis aute irure dolor in reprehend erit in voluptate velit esse cillum dolore eu fugiat nulla pariatur. Excepteur sint occaecat</p><a>LEARN MORE ➔</a></div>
  </article>
  <article class="abs card" style="left:618px;top:1754px">
    <div class="card-img" role="img" aria-label="Person doing yoga on a beach at sunset" style="background:linear-gradient(180deg,#f2c79a,#d58b58,#8a6a52)"></div>
    <div><h3>Lorem ipsum dolor sit amet, consectet ur adipiscing</h3><p>Duis aute irure dolor in reprehend erit in voluptate velit esse cillum dolore eu fugiat nulla pariatur. Excepteur sint occaecat</p><a>LEARN MORE ➔</a></div>
  </article>
  <article class="abs card" style="left:111px;top:2029px">
    <div class="card-img" role="img" aria-label="Lone tree backlit by golden sunlight" style="background:radial-gradient(circle at 50% 40%,#f6d27a,#b37a36 55%,#4a3420)"></div>
    <div><h3>Lorem ipsum dolor sit amet, consectet ur adipiscing</h3><p>Duis aute irure dolor in reprehend erit in voluptate velit esse cillum dolore eu fugiat nulla pariatur. Excepteur sint occaecat</p><a>LEARN MORE ➔</a></div>
  </article>
  <article class="abs card" style="left:618px;top:2029px">
    <div class="card-img" role="img" aria-label="Bird rising from an open hand with warm light" style="background:linear-gradient(160deg,#f3e0d0,#e3a98a,#c97a5a)"></div>
    <div><h3>Lorem ipsum dolor sit amet, consectet ur adipiscing</h3><p>Duis aute irure dolor in reprehend erit in voluptate velit esse cillum dolore eu fugiat nulla pariatur. Excepteur sint occaecat</p><a>LEARN MORE ➔</a></div>
  </article>

  <svg class="abs" style="left:0;top:2350px" width="1200" height="160" viewBox="0 0 1200 160">
    <path d="M0 60 C250 150 550 90 850 20 C1000 -5 1120 0 1200 10 V160 H0 Z" fill="var(--green)"/>
    <path d="M0 80 C250 170 560 120 860 50 C1010 20 1120 25 1200 40 V160 H0 Z" fill="#fff"/>
  </svg>
</section>

<section>
  <h2 class="abs heading section-title" style="top:2565px;color:#1f1f1f">Research Team</h2>
  <div class="abs member" style="left:123px;top:2639px"><div class="photo" role="img" aria-label="Portrait of a smiling team member" style="background:linear-gradient(160deg,#c9d3c4,#7c7a74)"></div><h4>John Doe</h4><span>Company name</span></div>
  <div class="abs member" style="left:366px;top:2639px"><div class="photo" role="img" aria-label="Portrait of a smiling team member" style="background:linear-gradient(160deg,#8a8f8c,#4f5a55);border:4px solid var(--green)"></div><h4>John Doe</h4><span>Company name</span></div>
  <div class="abs member" style="left:610px;top:2639px"><div class="photo" role="img" aria-label="Portrait of a smiling team member" style="background:linear-gradient(160deg,#b48d7a,#e8e4e0)"></div><h4>John Doe</h4><span>Company name</span></div>
  <div class="abs member" style="left:854px;top:2639px"><div class="photo" role="img" aria-label="Portrait of a smiling team member" style="background:linear-gradient(160deg,#9a9a9a,#6e6e6e)"></div><h4>John Doe</h4><span>Company name</span></div>
</section>

<section>
  <div class="abs faq-bg" role="img" aria-label="Green misty landscape backdrop"></div>
  <svg class="abs" style="left:0;top:3010px" width="1200" height="110" viewBox="0 0 1200 110">
    <path d="M0 0 H1200 V20 C900 30 600 110 300 100 C150 95 50 70 0 50 Z" fill="#fff"/>
    <path d="M0 50 C60 75 160 100 300 100 C520 100 700 40 830 10 C700 55 500 120 300 115 C150 112 60 90 0 70 Z" fill="var(--blue)"/>
  </svg>
  <h2 class="abs heading section-title" style="top:3152px;color:#fff">FAQs</h2>
  <div class="abs faq open" style="top:3231px"><span>1. What makes this project unique?</span><span class="plus">+</span></div>
  <div class="abs faq" style="top:3308px"><span>2. Does this project assume that the impact of religion is always positive?</span><span class="plus">+</span></div>
  <div class="abs faq" style="top:3385px"><span>3. How can I collaborate?</span><span class="plus">+</span></div>
  <div class="abs faq" style="top:3462px"><span>4. Will Fenmoor U faculty lead all projects?</span><span class="plus">+</span></div>
</section>

<footer>
  <div class="abs footer"></div>
  <svg class="abs" style="left:0;top:3600px" width="1200" height="120" viewBox="0 0 1200 120">
    <path d="M0 0 H1200 V70 C900 20 650 130 300 120 C180 117 80 100 0 85 Z" fill="#4a8a38"/>
    <path d="M0 85 C80 100 180 117 300 120 C650 130 900 20 1200 70 V80 C900 40 650 140 300 130 C170 127 80 110 0 95 Z" fill="#fff"/>
  </svg>
  <h3 class="abs foot-h" style="left:111px;top:3782px">GET IN TOUCH</h3>
  <div class="abs field" style="left:111px;top:3829px;width:235px">First Name</div>
  <div class="abs field" style="left:354px;top:3829px;width:235px">Last Name</div>
  <div class="abs field" style="left:111px;top:3878px;width:235px">Email</div>
  <div class="abs field" style="left:354px;top:3878px;width:235px">phone number</div>
  <div class="abs field" style="left:111px;top:3928px;width:478px;height:75px">Message</div>
  <a class="abs btn" style="left:111px;top:4021px;width:133px;height:46px;line-height:46px;font-size:15px;background:var(--green)">SUBMIT</a>

  <h3 class="abs foot-h" style="left:650px;top:3782px">QUICK LINKS</h3>
  <ul class="abs links" style="left:650px;top:3820px"><li>Home</li><li>About Us</li><li>Services</li><li>Contact Us</li><li>Privacy policy</li></ul>

  <h3 class="abs foot-h" style="left:847px;top:3782px">CONTACT US</h3>
  <div class="abs contact" style="left:850px;top:3828px"><svg width="12" height="16" viewBox="0 0 12 16"><path d="M6 0a6 6 0 0 0-6 6c0 4.5 6 10 6 10s6-5.5 6-10a6 6 0 0 0-6-6zm0 8.5A2.5 2.5 0 1 1 6 3.5a2.5 2.5 0 0 1 0 5z" fill="#fff"/></svg><span>270 Lorem ipsum dolor amet,<br>consectetur elit,</span></div>
  <div class="abs contact" style="left:850px;top:3884px"><svg width="10" height="16" viewBox="0 0 10 16"><rect x="1" y="1" width="8" height="14" rx="1.5" fill="none" stroke="#fff" stroke-width="1.8"/></svg><span>(05) 5501 2846</span></div>
  <div class="abs contact" style="left:850px;top:3918px"><svg width="16" height="15" viewBox="0 0 16 15"><rect x="1" y="4" width="14" height="10" fill="#fff"/><rect x="4" y="0" width="8" height="5" fill="none" stroke="#fff" stroke-width="1.6"/></svg><span>(05) 5501 9072</span></div>
  <div class="abs contact" style="left:850px;top:3952px"><svg width="16" height="12" viewBox="0 0 16 12"><rect x="1" y="1" width="14" height="10" fill="none" stroke="#fff" stroke-width="1.4"/><path d="M1 1l7 6 7-6" fill="none" stroke="#fff" stroke-width="1.4"/></svg><span>hello@quietharborloop.org</span></div>

  <h3 class="abs foot-h" style="left:650px;top:4010px">STAY CONNECTED :</h3>
  <div class="abs social" style="left:850px;top:4006px;background:#4a5fb0"></div>
  <div class="abs social" style="left:889px;top:4006px;background:#c23aa5"></div>

  <p class="abs" style="left:0;top:4132px;width:1200px;text-align:center;color:#fff;font-size:15px">© 2021 Company name &nbsp;| All Rights Reserved | Terms and Conditions</p>
</footer>

</body>
</html>
```